Business Card Design for a Personal Trainer

I need a business card design for my job as a personal trainer. It should have a unique, modern and exclusive design. On the front there should be only my logo with my name and my job. 0163/2918374 Tobias Hellwig Lindenkopfweg 14 80921 Munich Germany The most important contact information is the web adress. it can be bigger than the rest, but its not necessary. The card should be 8,5cmx5,5cm big. Font: Roboto. Colors: black, white, gray, 56c1ff.

```html
<!DOCTYPE html>
<html lang="de">
<head>
<meta charset="utf-8">
<title>Tobias Hellwig – Personal Trainer Visitenkarte</title>
<link rel="stylesheet" href="https://fonts.googleapis.com/css2?family=Roboto:wght@300;400;500;700&display=swap">
<style>
  :root {
    --bg: #2b2b2b;
    --card: #f3f3f3;
    --accent: #56c1ff;
    --ink: #2a2a2a;
    --gray: #9a9a9a;
    --photo-light: #d9d9d9;
    --photo-dark: #4a4a4a;
  }
  * { box-sizing: border-box; margin: 0; padding: 0; }
  html, body {
    width: 1200px; height: 764px; overflow: hidden;
    background: var(--bg);
    font-family: "Roboto", Arial, sans-serif;
  }
  .stage { position: relative; width: 1200px; height: 764px; }
  .card {
    position: absolute; top: 237px;
    width: 450px; height: 290px;
    background: var(--card);
    overflow: hidden;
  }
  .card--front { left: 118px; }
  .card--back { left: 632px; }

  /* Front */
  .brand {
    position: absolute; left: 0; right: 0; top: 88px;
    text-align: center;
  }
  .brand__mark {
    width: 34px; height: 34px; margin: 0 auto 16px;
    background: var(--accent);
  }
  .brand__name {
    color: var(--accent); font-weight: 400;
    font-size: 23px; letter-spacing: 0.3px;
    line-height: 1;
  }
  .brand__role {
    display: flex; align-items: center; justify-content: center;
    gap: 6px; margin-top: 5px;
    color: var(--accent); font-size: 9px; letter-spacing: 2.6px;
    font-weight: 400;
  }
  .brand__rule { width: 32px; height: 1px; background: var(--accent); }

  /* Back */
  .back__marker {
    position: absolute; left: 0; top: 54px; width: 7px; height: 28px;
    background: var(--accent);
  }
  .back__name {
    position: absolute; left: 27px; top: 54px;
    color: var(--accent); font-weight: 500; font-size: 15px; line-height: 1.1;
  }
  .back__role {
    position: absolute; left: 27px; top: 72px;
    color: var(--ink); font-size: 11.5px; font-weight: 400;
  }
  .contact {
    position: absolute; left: 28px; top: 164px;
    color: var(--ink); font-size: 12.5px; line-height: 18px;
    list-style: none;
  }
  .contact__item { display: flex; align-items: center; gap: 7px; }
  .contact__icon { width: 11px; height: 11px; flex: none; }
  .address {
    position: absolute; left: 28px; top: 204px;
    color: var(--ink); font-size: 12.5px; line-height: 18px; font-style: normal;
  }
  .web-band {
    position: absolute; left: 0; right: 0; bottom: 0; height: 45px;
    background: var(--accent);
  }
  .web-band__url {
    position: absolute; left: 30px; top: 13px;
    color: #fff; font-size: 15px; font-weight: 400; letter-spacing: 0.2px;
  }
  .web-band__url strong { font-weight: 700; }
  .portrait {
    position: absolute; right: 6px; top: 12px; width: 190px; height: 278px;
    background: linear-gradient(180deg, var(--photo-light) 0%, #8a8a8a 35%, var(--photo-dark) 100%);
  }
</style>
</head>
<body>
<main class="stage">
  <section class="card card--front" aria-label="Vorderseite">
    <div class="brand">
      <div class="brand__mark"></div>
      <div class="brand__name">TOBIAS HELLWIG</div>
      <div class="brand__role">
        <span class="brand__rule"></span>PERSONAL TRAINER<span class="brand__rule"></span>
      </div>
    </div>
  </section>

  <section class="card card--back" aria-label="Rückseite">
    <div class="back__marker"></div>
    <h1 class="back__name">TOBIAS HELLWIG</h1>
    <p class="back__role">PERSONAL TRAINER</p>

    <ul class="contact">
      <li class="contact__item">
        <svg class="contact__icon" viewBox="0 0 12 12" aria-hidden="true">
          <rect width="12" height="12" rx="1.5" fill="var(--accent)"/>
          <path d="M3.5 2.8 L5 4.6 L4.2 5.4 Q5.2 7.2 6.7 7.9 L7.5 7.1 L9.2 8.6 L8.2 9.6 Q4.5 9 2.6 3.8 Z" fill="#fff"/>
        </svg>0163/2918374
      </li>
      <li class="contact__item">
        <svg class="contact__icon" viewBox="0 0 12 12" aria-hidden="true">
          <rect width="12" height="12" rx="1.5" fill="var(--accent)"/>
          <rect x="2.5" y="3.5" width="7" height="5" fill="none" stroke="#fff" stroke-width="1"/>
          <path d="M2.5 3.5 L6 6.3 L9.5 3.5" fill="none" stroke="#fff" stroke-width="1"/>
        </svg>T.HELLWIG@POSTFELD.DE
      </li>
    </ul>

    <address class="address">LINDENKOPFWEG 14<br>80921 MÜNCHEN</address>

    <div class="web-band">
      <span class="web-band__url">WWW.<strong>HELLWIGTRAINING</strong>.DE</span>
    </div>

    <div class="portrait" role="img" aria-label="Schwarzweiß-Porträt des Trainers mit verschränkten Armen im dunklen Sportshirt"></div>
  </section>
</main>
</body>
</html>
```